This is for a poster that will be hanging in the window of a Men's Suit Store in the mall:
Size 4 feet wide by 6 feet high
Main point is: A sale on "Suits" or "Men's Suits" at 40%-60% off ( the 40%-60% off should be the focal point)
Some words that can be used are "Sale" or "Clearance Sale"
Some key words that can be used to make it urgent are "limited time offer" or something similar.
You can get creative, the point is for the customer to want to come into the store and buy a suit right away.
You may use a graphic (picture of a man in a suit). It is not necessary but if it looks good you can use it. (If you do use a picture, it should be of a modern fit or slim fit suit)
Sorry, the initial brief somehow got deleted from the project. Please see the updated brief.
Thanks
Reason: Project was closed for some reason, extended to give enough time to complete
Target Market(s)
Mostly Men ages 35-55
Industry/Entity Type
Store
Colors
Designer to choose colors to be used in the design.

```html
<!DOCTYPE html>
<html lang="en">
<head>
<meta charset="UTF-8">
<title>Men's Suits Sale Poster</title>
<link rel="stylesheet" href="https://fonts.googleapis.com/css2?family=Urbanist:wght@600;700;800&display=swap">
<style>
  :root {
    --canvas-bg: #ffffff;
    --poster-black: #050505;
    --poster-sheen: #1c1c1c;
    --silver-light: #ffffff;
    --silver-mid: #e4e4e4;
    --silver-dark: #9a9a9a;
  }
  html, body {
    margin: 0;
    padding: 0;
    width: 1200px;
    height: 1000px;
    overflow: hidden;
    background: var(--canvas-bg);
  }
  .canvas {
    position: relative;
    width: 1200px;
    height: 1000px;
    font-family: "Urbanist", "Century Gothic", sans-serif;
  }
  .poster {
    position: absolute;
    left: 354px;
    top: 136px;
    width: 492px;
    height: 728px;
    background:
      radial-gradient(ellipse 220px 140px at 90px 540px, var(--poster-sheen), transparent 70%),
      radial-gradient(ellipse 200px 120px at 330px 700px, #161616, transparent 70%),
      var(--poster-black);
    overflow: hidden;
  }
  .silver {
    position: absolute;
    margin: 0;
    line-height: 1;
    white-space: nowrap;
    font-weight: 700;
    background: linear-gradient(180deg, var(--silver-light) 0%, var(--silver-mid) 45%, var(--silver-dark) 100%);
    -webkit-background-clip: text;
    background-clip: text;
    color: transparent;
  }
  .headline {
    left: 0;
    width: 100%;
    top: -14px;
    text-align: center;
    font-size: 192px;
    font-weight: 800;
    letter-spacing: -4px;
  }
  .category {
    left: 0;
    width: 100%;
    top: 152px;
    text-align: center;
    font-size: 70px;
  }
  .discount {
    font-size: 166px;
    font-weight: 700;
    letter-spacing: -2px;
  }
  .discount-low { left: 16px; top: 242px; }
  .discount-high { left: 172px; top: 377px; }
  .off-label {
    left: 160px;
    top: 535px;
    font-size: 100px;
  }
  .urgency {
    left: 0;
    width: 100%;
    top: 655px;
    text-align: center;
    font-size: 58px;
  }
</style>
</head>
<body>
  <div class="canvas">
    <section class="poster">
      <h1 class="silver headline">SALE</h1>
      <h2 class="silver category">Men’s Suits</h2>
      <p class="silver discount discount-low">40%</p>
      <p class="silver discount discount-high">60%</p>
      <p class="silver off-label">OFF</p>
      <p class="silver urgency">Short Time Only!</p>
    </section>
  </div>
</body>
</html>
```